Tunnel

a graphic meme to be sent to my clients, consisting of a long angular dark tunnel with a bright light at one end; located within the bright light at the end of the tunnel is the number 2021
the illuminated (shiny silver?) 3 dimensional font message running along the left wall of the tunnel is: BE SAFE.!
the smaller font message underneath the graphic is: Best Wishes For a Healthy New Year
Dan Marlowe Mediator (also to be included nearby is a small semi-circle logo of my corporate logo).

Font styles to use
Sans Serif
Other font styles liked:
• 3 dimensional bold lettering for BE SAFE

```html
<!DOCTYPE html>
<html lang="en">
<head>
<meta charset="utf-8">
<title>Best Wishes For a Healthy New Year – Dan Marlowe Mediator</title>
<link href="https://fonts.googleapis.com/css2?family=Arimo:wght@700&display=swap" rel="stylesheet">
<style>
  :root {
    --ink: #161616;
    --brand: #2b1b10;
    --tunnel-light: #ffffff;
    --tunnel-mid: #b9b9b9;
    --tunnel-edge: #8a8a8a;
    --tunnel-dark: #4a4a4a;
    --shadow-letters: rgba(70, 70, 70, 0.55);
  }
  html, body {
    margin: 0;
    padding: 0;
    width: 1200px;
    height: 792px;
    overflow: hidden;
    background: #ffffff;
  }
  .greeting-card {
    position: relative;
    width: 1200px;
    height: 792px;
    overflow: hidden;
    font-family: "Arimo", Arial, sans-serif;
    font-weight: 700;
  }
  .greeting-card svg {
    display: block;
  }
  .arched-wish {
    fill: var(--ink);
    font-size: 60px;
  }
  .year-number {
    fill: var(--ink);
    font-size: 76px;
  }
  .be-safe-shadow {
    fill: var(--shadow-letters);
    font-size: 58px;
  }
  .brand-name {
    fill: var(--brand);
    font-size: 24px;
  }
  .firm-name {
    fill: var(--brand);
    font-size: 10px;
  }
  .firm-circle {
    fill: none;
    stroke: var(--brand);
    stroke-width: 1.5;
  }
</style>
</head>
<body>
<main class="greeting-card">
  <svg width="1200" height="792" viewBox="0 0 1200 792" xmlns="http://www.w3.org/2000/svg">
    <defs>
      <radialGradient id="tunnelGlow" cx="595" cy="530" r="720" gradientUnits="userSpaceOnUse">
        <stop offset="0" stop-color="var(--tunnel-light)"/>
        <stop offset="0.14" stop-color="var(--tunnel-light)"/>
        <stop offset="0.2" stop-color="var(--tunnel-dark)"/>
        <stop offset="0.45" stop-color="var(--tunnel-edge)"/>
        <stop offset="0.75" stop-color="var(--tunnel-mid)"/>
        <stop offset="1" stop-color="#dcdcdc"/>
      </radialGradient>
      <linearGradient id="floorShade" x1="0" y1="0" x2="0" y2="1">
        <stop offset="0" stop-color="#6a6a6a" stop-opacity="0"/>
        <stop offset="1" stop-color="#3a3a3a" stop-opacity="0.55"/>
      </linearGradient>
      <path id="wishArc" d="M 200 560 A 395 395 0 0 1 990 560"/>
      <filter id="softShadow"><feGaussianBlur stdDeviation="1.6"/></filter>
    </defs>

    <g class="tunnel-backdrop" role="img" aria-label="Photograph of a long corrugated metal tunnel with ceiling lights, bright light shining at the far end">
      <rect width="1200" height="792" fill="url(#tunnelGlow)"/>
      <rect y="600" width="1200" height="192" fill="url(#floorShade)"/>
    </g>

    <g class="brand-header">
      <text class="firm-name" x="402" y="44" text-anchor="end">Harlan Pierce Group</text>
      <circle class="firm-circle" cx="442" cy="40" r="20"/>
      <text class="brand-name" x="497" y="49">Dan Marlowe Mediator</text>
    </g>

    <text class="arched-wish">
      <textPath href="#wishArc" textLength="1235" lengthAdjust="spacing">Best Wishes For a Healthy New Year</textPath>
    </text>

    <text class="year-number" x="594" y="616" text-anchor="middle">2021</text>

    <text class="be-safe-shadow" filter="url(#softShadow)"
          transform="translate(590 622) scale(1.25 -1.1) skewX(-10)" text-anchor="middle" x="0" y="-54">BE SAFE</text>
  </svg>
</main>
</body>
</html>
```